Disability Service Provider needs a flyer

Project Description:
We are seeking a creative and engaging flyer design to promote a twelve week independent living skills program, focusing on key areas such as money management, basic cooking, food safety, and personal well-being and interpersonal skills. The flyer will be used to encourage individuals to enhance their abilities to live independently and confidently.

Target Audience:
Our target audience includes young adults with a disability and individuals transitioning into independent living situations. We aim to reach those who may be new to managing their own finances, cooking for themselves, and maintaining a healthy lifestyle.

Key Messages:

Independent Living Skills: Emphasize the importance of acquiring essential skills for independent living.
Money Management: Highlight budgeting tips, saving strategies, and financial planning.
Basic Cooking: Showcase simple recipes, cooking techniques, and meal preparation tips.
Food Safety: Provide information on safe food handling practices, storage guidelines, and hygiene.
Personal Well-being: Promote self-care practices, stress management techniques, and mental health awareness.

Target Market(s)

Young adults looking to live independently on their own or with friends

Industry/Entity Type

community services sector

Colors
0054AA
0677BA
7BADD7
CADEEF
E8F1F8

Requirements
Must have
• refer to brief

```html
<!DOCTYPE html>
<html lang="en">
<head>
<meta charset="utf-8">
<title>Brightpath Care – Independent Living Flyer</title>
<link rel="stylesheet" href="https://fonts.googleapis.com/css2?family=Archivo+Black&family=Poppins:wght@400;600;700&display=swap">
<style>
:root{
  --navy:#0f4566;
  --deep:#135a80;
  --bright:#1a8fc6;
  --sky:#7badd7;
  --mist:#e8f1f8;
  --paper:#ffffff;
  --ink:#1b2430;
  --stage:#e9edf1;
}
*{margin:0;padding:0;box-sizing:border-box}
html,body{width:1200px;height:1177px;overflow:hidden;background:var(--stage)}
.flyer-frame{position:absolute;left:167px;top:28px;width:866px;height:1120px;overflow:hidden;box-shadow:0 6px 24px rgba(0,0,0,.15)}
.flyer{position:absolute;left:0;top:0;width:1254px;height:1623px;transform:scale(.6903);transform-origin:0 0;
  background:linear-gradient(180deg,var(--paper) 0%,var(--mist) 60%,var(--paper) 100%);font-family:'Poppins',sans-serif;color:var(--ink)}
.art{position:absolute;left:0;top:0;width:1254px;height:1623px}
.brand{position:absolute;left:120px;top:78px;display:flex;align-items:center;gap:16px;font-family:'Poppins',sans-serif;font-weight:700;font-size:46px;line-height:60px;color:var(--navy);letter-spacing:-1px;white-space:nowrap}
.brand-dot{width:40px;height:40px;border-radius:50%;background:var(--navy)}
.tagline{position:absolute;left:678px;top:55px;font-family:'Archivo Black',sans-serif;font-size:31px;line-height:35px;color:#fff;letter-spacing:.5px;white-space:nowrap}
.service{position:absolute;width:480px}
.service-badge{position:absolute;left:0;top:0;width:104px;height:104px;border-radius:50%;background:var(--bright);border:6px solid #fff;box-shadow:0 2px 8px rgba(0,0,0,.12);z-index:2}
.service-title{position:absolute;left:90px;top:14px;width:377px;height:78px;border:1.5px solid var(--bright);border-left:none;border-radius:0 40px 40px 0;background:#fff;
  display:flex;align-items:center;padding-left:34px;font-weight:700;font-size:23px;color:var(--navy);white-space:nowrap}
.service-title.is-wide{width:404px}
.service-text{position:absolute;left:124px;top:118px;font-size:20.5px;line-height:27.5px;color:var(--ink);white-space:nowrap}
.connector{position:absolute;width:2px;background:var(--navy)}
.connector::after{content:"";position:absolute;left:-6px;top:50%;margin-top:-7px;width:14px;height:14px;border-radius:50%;background:var(--bright)}
.contact-bar{position:absolute;left:673px;top:1322px;width:581px;height:51px;background:var(--navy);border-radius:26px 0 0 26px;
  font-family:'Poppins',sans-serif;font-weight:700;font-size:31px;color:#fff;padding-left:52px;line-height:51px;letter-spacing:.5px}
.contact-list{position:absolute;left:724px;top:1386px;font-size:21px;line-height:28px;color:var(--ink);list-style:none;white-space:nowrap}
.contact-list li{display:flex;align-items:flex-start;gap:14px;margin-bottom:6px}
.contact-list svg{flex:none;margin-top:5px}
.contact-inline{display:flex;gap:12px;align-items:flex-start}
</style>
</head>
<body>
<div class="flyer-frame">
<div class="flyer">
  <svg class="art" viewBox="0 0 1254 1623">
    <defs>
      <linearGradient id="photoTone" x1="0" y1="0" x2="0" y2="1">
        <stop offset="0" stop-color="#8a9a6a"/>
        <stop offset=".55" stop-color="#55604a"/>
        <stop offset="1" stop-color="#c9c2b2"/>
      </linearGradient>
      <linearGradient id="bandDeep" x1="0" y1="0" x2="1" y2="0">
        <stop offset="0" stop-color="#1a8fc6"/>
        <stop offset=".5" stop-color="#135a80"/>
        <stop offset="1" stop-color="#0f4566"/>
      </linearGradient>
    </defs>
    <path d="M0,165 C200,205 420,205 630,180 C600,110 600,30 650,0 H1254 V290 C1000,205 700,212 400,228 C250,234 100,218 0,190 Z" fill="url(#bandDeep)"/>
    <path role="img" aria-label="Photo: three smiling young men in wheelchairs sitting side by side outdoors among trees" d="M0,192 C150,225 300,240 500,232 C750,222 1000,215 1254,290 V778 C1000,758 700,768 450,800 C250,822 100,765 0,612 Z" fill="url(#photoTone)"/>
    <path d="M0,612 C100,765 250,822 450,800 C700,768 1000,758 1254,778 V790 C1000,775 700,785 450,815 C250,838 90,790 0,690 Z" fill="#fff"/>
    <path d="M0,690 C90,790 250,838 450,815 C700,785 1000,775 1254,790 V920 C1100,830 850,812 560,818 C300,822 100,808 0,740 Z" fill="url(#bandDeep)"/>
    <path d="M0,740 C100,808 300,822 560,818 C850,812 1100,830 1254,920 V935 C1100,850 850,830 560,836 C300,840 100,826 0,760 Z" fill="#fff"/>
    <path d="M1254,1400 C1220,1480 1150,1556 1000,1578 C700,1560 300,1500 0,1525 V1623 H1254 Z" fill="url(#bandDeep)"/>
    <path d="M1254,1470 C1180,1540 1080,1572 900,1586 C600,1572 300,1560 0,1575 V1623 H1254 Z" fill="#fff"/>
    <path d="M1254,1490 C1180,1556 1080,1590 900,1598 C600,1590 300,1578 0,1590 V1623 H1254 Z" fill="var(--bright)"/>
  </svg>

  <div class="brand"><span class="brand-dot"></span>Brightpath Care</div>
  <div class="tagline">YOUR TRUSTED PARTNER IN<br>DISABILITY &amp; INDEPENDENT<br>LIVING SUPPORT SERVICES.</div>

  <div class="connector" style="left:155px;top:993px;height:88px"></div>
  <div class="connector" style="left:155px;top:1193px;height:90px"></div>
  <div class="connector" style="left:729px;top:993px;height:88px"></div>

  <section class="service" style="left:104px;top:883px">
    <div class="service-badge"></div>
    <h2 class="service-title is-wide">Independent Living Skills</h2>
    <p class="service-text">Emphasize the importance<br>of acquiring essential skills<br>for independent living.</p>
  </section>
  <section class="service" style="left:104px;top:1083px">
    <div class="service-badge"></div>
    <h2 class="service-title">Money Management</h2>
    <p class="service-text" style="top:132px">Highlight budgeting tips, saving<br>strategies, and financial planning.</p>
  </section>
  <section class="service" style="left:104px;top:1285px">
    <div class="service-badge"></div>
    <h2 class="service-title">Basic Cooking</h2>
    <p class="service-text">Showcase simple recipes,<br>cooking techniques, and meal<br>preparation tips.</p>
  </section>
  <section class="service" style="left:678px;top:883px">
    <div class="service-badge"></div>
    <h2 class="service-title">Food Safety</h2>
    <p class="service-text">Provide information on safe food<br>handling practices, storage<br>guidelines, and hygiene.</p>
  </section>
  <section class="service" style="left:678px;top:1083px">
    <div class="service-badge"></div>
    <h2 class="service-title">Personal Well-being</h2>
    <p class="service-text" style="top:132px">Promote self-care practices,<br>stress management techniques,<br>and mental health awareness.</p>
  </section>

  <div class="contact-bar">CONTACT US</div>
  <ul class="contact-list">
    <li><span class="contact-inline">
      <svg width="20" height="20" viewBox="0 0 20 20"><circle cx="10" cy="10" r="10" fill="var(--bright)"/><path d="M6.5,5.5 l2,0 l1,2.5 -1.3,1 a6,6 0 0 0 2.8,2.8 l1,-1.3 2.5,1 0,2 a1,1 0 0 1 -1,1 a8,8 0 0 1 -8,-8 a1,1 0 0 1 1,-1z" fill="#fff"/></svg>
      <span>1300 555 019</span>
      <svg width="20" height="20" viewBox="0 0 20 20"><circle cx="10" cy="10" r="10" fill="var(--bright)"/><circle cx="10" cy="10" r="5" fill="none" stroke="#fff" stroke-width="1.4"/><path d="M5,10 h10 M10,5 c-2.5,3 -2.5,7 0,10 M10,5 c2.5,3 2.5,7 0,10" fill="none" stroke="#fff" stroke-width="1.2"/></svg>
      <span>brightpathcare.example</span></span></li>
    <li><svg width="20" height="20" viewBox="0 0 20 20"><circle cx="10" cy="10" r="10" fill="var(--bright)"/><rect x="5" y="6.5" width="10" height="7" rx="1" fill="none" stroke="#fff" stroke-width="1.4"/><path d="M5.5,7 l4.5,3.5 4.5,-3.5" fill="none" stroke="#fff" stroke-width="1.4"/></svg><span>info@brightpathcare.example</span></li>
    <li><svg width="20" height="22" viewBox="0 0 20 22"><path d="M10,1 a8,8 0 0 1 8,8 c0,6 -8,12 -8,12 c0,0 -8,-6 -8,-12 a8,8 0 0 1 8,-8z" fill="var(--bright)"/><circle cx="10" cy="9" r="3" fill="#fff"/></svg><span>8/14 Harbour Lane, Riverside<br>Heights QLD 4000</span></li>
  </ul>
</div>
</div>
</body>
</html>
```